An ecommerce website needs a Home page design.

We need a home page design (uncoded) for an ecommerce store. The e-Store will be run by an exhibition gallery business.

About Company:

The company is into the business of renting out physical space for exhibitors. These exhibitors showcase their lifestyle products which range from apparels (ethic & western), jewelry, ceramics, hand made art objects, accessories, Bags, Footwear.

Company website - http://www.marlowhall.biz/

About e-Store:

The company is now looking to create an online store that will have products from exhibitors. So in a way it will be like a marketplace where multiple vendors (in our case exhibitors) sell their products.

Design Requirements:

We need home page design (uncoded) for the online store as mentioned above. The final design should communicate class, premium, luxury, lifestyle.

The look & feel can be similar to https://in.quenvale.com/. Of course, obviously would want distinctness.

For reference, I have attached a wireframe depicting the elements that will go on home page. The wireframe is for reference sake only.

Final design MAY NOT follow exact structure, though elements will remain the same. Here, Creativity of designer will be appreciated.

Also attaching the logo in PNG format.

Target Market(s)

Upper Middle Class, High Class Women

Industry/Entity Type

Business

Number of Pages Required

1 page

Requirements
Must have
• Premium, Luxury look

```html
<!DOCTYPE html>
<html lang="en">
<head>
<meta charset="utf-8">
<title>Marlow Hall – Home</title>
<link rel="stylesheet" href="https://fonts.googleapis.com/css2?family=Lato:wght@400;700;900&family=Playfair+Display:wght@400;700&display=swap">
<style>
:root{
  --ink:#2a2a2a;
  --nav:#262626;
  --orange:#f39322;
  --orange-deep:#e2662a;
  --muted:#8a8a8a;
  --line:#d9d9d9;
  --paper:#ffffff;
  --footer:#ececec;
}
*{box-sizing:border-box;margin:0;padding:0}
html,body{width:1200px;height:2912px;overflow:hidden}
body{background:var(--paper);font-family:"Lato",sans-serif;color:var(--ink);position:relative}
.wrap{width:1056px;margin:0 auto;position:relative}

/* header */
.topbar{height:84px;position:relative}
.brand{position:absolute;left:72px;top:22px;display:flex;align-items:center;gap:10px;font-family:"Lato",sans-serif;font-weight:700;font-size:30px;color:var(--ink)}
.brand .dot{width:14px;height:14px;background:var(--orange)}
.search{position:absolute;right:72px;top:12px;width:230px;height:24px;border:1px solid var(--line);font-size:11px;color:var(--muted);padding:5px 8px}
.account{position:absolute;right:72px;top:56px;display:flex;gap:16px;font-size:10px;font-weight:700;color:#555;letter-spacing:.3px}
.mainnav{height:48px;background:var(--nav);display:flex;align-items:stretch;padding-left:72px}
.mainnav a{color:#eee;text-decoration:none;font-size:14px;font-weight:700;letter-spacing:.6px;padding:0 16px;display:flex;align-items:center}
.mainnav a.hot{background:var(--orange);color:#fff;margin-left:auto;margin-right:72px}

/* hero */
.hero{height:428px;display:flex}
.hero-main{width:780px;position:relative;background:linear-gradient(160deg,#3b2616,#8a4a23 45%,#c23b2a 70%,#2a1a12)}
.hero-title{position:absolute;left:28px;bottom:36px;color:#fff;font-family:"Playfair Display",serif;font-weight:700;line-height:1}
.hero-title small{display:block;font-size:30px;font-style:normal}
.hero-title span{font-size:58px;letter-spacing:1px}
.hero-side{flex:1;position:relative;background:linear-gradient(180deg,#d7c6a8,#b49c78 55%,#6e5a44)}
.visit{position:absolute;right:26px;bottom:28px;background:#1e1e1e;color:#fff;font-size:12px;font-weight:700;padding:8px 14px;letter-spacing:.3px}

/* section headings */
.sec-head{display:flex;align-items:center;gap:18px;width:1056px;margin:0 auto}
.sec-head::before,.sec-head::after{content:"";flex:1;border-top:3px double #bdbdbd}
.sec-head h2{font-family:"Playfair Display",serif;font-weight:700;font-size:26px;letter-spacing:1px}

.tiles{display:flex;gap:14px;width:1056px;margin:0 auto}
.tile{flex:1;position:relative}
.tile .art{height:100%}
.tile .cap{position:absolute;left:12px;bottom:12px;color:#fff;font-size:17px;font-weight:700;line-height:1.15}
.tile .cap small{display:block;font-size:11px;font-weight:400;opacity:.85}

.exhibitors{position:absolute;top:588px;left:0;width:1200px}
.exhibitors .tiles{margin-top:26px;height:276px}
.categories{position:absolute;top:976px;left:0;width:1200px}
.categories .tiles{margin-top:36px;height:268px}

/* products */
.tabs{position:absolute;top:1384px;left:72px;width:1056px;height:48px;border-bottom:2px solid var(--ink);display:flex;gap:4px;align-items:flex-end}
.tabs span{font-family:"Playfair Display",serif;font-size:19px;padding:10px 18px;border:1px solid var(--ink);border-bottom:none}
.tabs .on{background:var(--ink);color:#fff}
.products{position:absolute;top:1480px;left:72px;width:1056px;display:flex;gap:18px}
.card{flex:1;border:1px solid var(--line);height:380px;padding:12px}
.card .art{height:190px;margin-bottom:14px}
.card .name{font-size:13px;font-weight:700}
.card .price{font-size:12px;color:var(--orange-deep);margin:4px 0 10px}
.card .price s{color:var(--muted);margin-left:4px}
.cart{display:flex;align-items:center;justify-content:space-between;border:1px solid var(--orange);color:var(--orange-deep);font-size:12px;font-weight:900;padding:7px 10px}
.card .util{display:flex;justify-content:space-between;margin-top:14px;font-size:11px;color:var(--muted)}
.card .util span{display:flex;align-items:center;gap:5px}

/* sell banner */
.sell{position:absolute;top:1912px;left:72px;width:1056px;height:356px;background:radial-gradient(circle at 30% 40%,#e7b53a,#2f6fa6 40%,#c54a2d 70%,#2b3e56)}
.sell-box{position:absolute;left:50%;bottom:18px;transform:translateX(-50%);background:rgba(20,20,20,.88);color:#fff;text-align:center;padding:14px 34px;font-weight:900;letter-spacing:.8px}
.sell-box b{display:block;font-size:19px;margin-bottom:6px}
.sell-box span{font-size:15px}

/* newsletter */
.news{position:absolute;top:2372px;left:0;width:1200px;height:188px;background:var(--orange)}
.news-badge{position:absolute;left:576px;top:-28px;width:48px;height:48px;border-radius:50%;background:#333;display:flex;align-items:center;justify-content:center}
.news p{position:absolute;top:54px;width:100%;text-align:center;font-size:17px;font-weight:700;color:#3a2410}
.news form{position:absolute;top:104px;left:346px;display:flex}
.news .field{width:354px;height:44px;background:#fff;font-size:14px;color:var(--muted);padding:13px 14px}
.news .go{width:160px;height:44px;background:var(--orange-deep);color:#fff;font-weight:700;font-size:16px;display:flex;align-items:center;justify-content:center}

/* footer */
.foot{position:absolute;top:2560px;left:0;width:1200px;height:352px;background:var(--footer)}
.cols{position:absolute;top:46px;left:112px;display:flex;gap:54px}
.col h4{font-size:14px;font-weight:700;letter-spacing:.5px;border-bottom:1px solid #bbb;padding-bottom:5px;margin-bottom:10px}
.col li{list-style:none;font-size:12px;color:#555;line-height:20px}
.social{display:flex;gap:8px;flex-wrap:wrap;width:92px}
.social i{width:22px;height:22px;border-radius:50%;background:#555;display:block}
.cards{display:grid;grid-template-columns:repeat(3,38px);gap:6px}
.cards i{height:24px;background:#c9c9c9;border:1px solid #aaa;display:block}
.copy{position:absolute;bottom:24px;width:100%;text-align:center;font-size:12px;color:#666}
</style>
</head>
<body>

<header class="topbar">
  <div class="brand"><span>Marlow Hall</span><i class="dot"></i></div>
  <div class="search">Search Marlow Hall…</div>
  <nav class="account"><span>MY ACCOUNT</span><span>MY WISHLIST</span><span>MY CART</span><span>CHECKOUT</span><span>LOGIN</span></nav>
</header>
<nav class="mainnav">
  <a>CLOTHING</a><a>JEWELRY</a><a>BAGS</a><a>FOOTWEAR</a><a>ACCESSORIES</a><a>HOME &amp; DECOR</a><a>HANDMADE</a><a>NGO</a><a class="hot">ALL EXHIBITORS</a>
</nav>

<section class="hero">
  <div class="hero-main" role="img" aria-label="Row of colourful handmade string puppets">
    <div class="hero-title"><small>HAND</small><span>MADE ART</span></div>
  </div>
  <div class="hero-side" role="img" aria-label="Entrance of the Marlow Hall exhibition gallery">
    <div class="visit">VISIT US IN AHMEDABAD</div>
  </div>
</section>

<section class="exhibitors">
  <div class="sec-head"><h2>FEATURED EXHIBITORS</h2></div>
  <div class="tiles">
    <div class="tile"><div class="art" role="img" aria-label="Folded silk sarees in bright colours" style="background:linear-gradient(135deg,#c0245a,#e08a2e,#2d6fb0)"></div><div class="cap">Ambrika<small>Ahmedabad</small></div></div>
    <div class="tile"><div class="art" role="img" aria-label="Model in red bridal wear" style="background:linear-gradient(160deg,#5a1410,#b3261e,#e0a070)"></div><div class="cap">Devansh<small>Mumbai</small></div></div>
    <div class="tile"><div class="art" role="img" aria-label="Model in western clothing" style="background:linear-gradient(160deg,#9a9590,#6b4c3a,#2e2a28)"></div><div class="cap">Tarini Clothing<small>Vadodara</small></div></div>
    <div class="tile"><div class="art" role="img" aria-label="Model with colourful jewellery and headwrap" style="background:linear-gradient(160deg,#1e6e8a,#c43b2e,#e7b03a)"></div><div class="cap">Hooghly Jewellers<small>Kolkata</small></div></div>
    <div class="tile"><div class="art" role="img" aria-label="Cane handicraft pieces" style="background:linear-gradient(160deg,#cdbfae,#8c7a66,#5a4b3c)"></div><div class="cap">Veni Cane<small>Ahmedabad</small></div></div>
  </div>
</section>

<section class="categories">
  <div class="sec-head"><h2>TOP CATEGORIES</h2></div>
  <div class="tiles">
    <div class="tile"><div class="art" role="img" aria-label="Bride in traditional attire" style="background:linear-gradient(160deg,#7a1a1a,#c8402c,#e8b46a)"></div><div class="cap">Bridal</div></div>
    <div class="tile"><div class="art" role="img" aria-label="Women in colourful Indian dress" style="background:linear-gradient(160deg,#3c6aa8,#d05a2a,#e9c24a)"></div><div class="cap">Indian</div></div>
    <div class="tile"><div class="art" role="img" aria-label="Hanging embroidered handicrafts" style="background:linear-gradient(160deg,#2a7a56,#d9402a,#f0b830)"></div><div class="cap">Handicrafts</div></div>
    <div class="tile"><div class="art" role="img" aria-label="Model wearing statement jewellery" style="background:linear-gradient(160deg,#3a3a44,#8a6a58,#c9ab8e)"></div><div class="cap">Fashion Jewelry</div></div>
    <div class="tile"><div class="art" role="img" aria-label="Stacked sarees" style="background:linear-gradient(160deg,#d8d0c4,#9f2f4e,#3a6aa0)"></div><div class="cap">Sarees</div></div>
  </div>
</section>

<div class="tabs"><span class="on">BEST SELLERS</span><span>NEW ARRIVALS</span></div>

<section class="products">
  <article class="card"><div class="art" role="img" aria-label="Set of green jewellery boxes" style="background:linear-gradient(160deg,#dfe7e2,#3f6e5c)"></div><div class="name">Product 1 Name</div><div class="price">Rs. 9,999.00</div><div class="cart">ADD TO CART<svg width="16" height="14" viewBox="0 0 16 14"><path d="M1 1h3l2 8h8l1-6H5" fill="none" stroke="currentColor" stroke-width="1.5"/><circle cx="7" cy="12" r="1.3" fill="currentColor"/><circle cx="13" cy="12" r="1.3" fill="currentColor"/></svg></div><div class="util"><span>♡ Add To Wishlist</span><span>⇄ Add To Compare</span></div></article>
  <article class="card"><div class="art" role="img" aria-label="Green and red saree on model" style="background:linear-gradient(160deg,#f0f0ec,#3d8a3a,#b23028)"></div><div class="name">Product 2 Name</div><div class="price">Rs. 9,999.00</div><div class="cart">ADD TO CART<svg width="16" height="14" viewBox="0 0 16 14"><path d="M1 1h3l2 8h8l1-6H5" fill="none" stroke="currentColor" stroke-width="1.5"/><circle cx="7" cy="12" r="1.3" fill="currentColor"/><circle cx="13" cy="12" r="1.3" fill="currentColor"/></svg></div><div class="util"><span>♡ Add To Wishlist</span><span>⇄ Add To Compare</span></div></article>
  <article class="card"><div class="art" role="img" aria-label="Gold bead bracelet" style="background:linear-gradient(160deg,#ffffff,#e6c88a,#a8782c)"></div><div class="name">Product 3 Name</div><div class="price">Rs. 9,999.00</div><div class="cart">ADD TO CART<svg width="16" height="14" viewBox="0 0 16 14"><path d="M1 1h3l2 8h8l1-6H5" fill="none" stroke="currentColor" stroke-width="1.5"/><circle cx="7" cy="12" r="1.3" fill="currentColor"/><circle cx="13" cy="12" r="1.3" fill="currentColor"/></svg></div><div class="util"><span>♡ Add To Wishlist</span><span>⇄ Add To Compare</span></div></article>
  <article class="card"><div class="art" role="img" aria-label="Hanging patterned pendant lamps" style="background:linear-gradient(160deg,#ffffff,#9a9a9a,#3a3a3a)"></div><div class="name">Product 4 Name</div><div class="price">Rs. 9,999.00</div><div class="cart">ADD TO CART<svg width="16" height="14" viewBox="0 0 16 14"><path d="M1 1h3l2 8h8l1-6H5" fill="none" stroke="currentColor" stroke-width="1.5"/><circle cx="7" cy="12" r="1.3" fill="currentColor"/><circle cx="13" cy="12" r="1.3" fill="currentColor"/></svg></div><div class="util"><span>♡ Add To Wishlist</span><span>⇄ Add To Compare</span></div></article>
  <article class="card"><div class="art" role="img" aria-label="Painted ceramic vase" style="background:linear-gradient(160deg,#ffffff,#e8e4e6,#c0728a)"></div><div class="name">Product 5 Name</div><div class="price">Rs. 9,999.00</div><div class="cart">ADD TO CART<svg width="16" height="14" viewBox="0 0 16 14"><path d="M1 1h3l2 8h8l1-6H5" fill="none" stroke="currentColor" stroke-width="1.5"/><circle cx="7" cy="12" r="1.3" fill="currentColor"/><circle cx="13" cy="12" r="1.3" fill="currentColor"/></svg></div><div class="util"><span>♡ Add To Wishlist</span><span>⇄ Add To Compare</span></div></article>
</section>

<section class="sell" role="img" aria-label="Display of hand-painted ceramic plates">
  <div class="sell-box"><b>SELL WITH US</b><span>BECOME AN EXHIBITOR ON MARLOW HALL</span></div>
</section>

<section class="news">
  <div class="news-badge"><svg width="24" height="18" viewBox="0 0 24 18"><rect x="1" y="1" width="22" height="16" fill="var(--orange)"/><path d="M1 1l11 9 11-9" fill="none" stroke="#333" stroke-width="1.6"/></svg></div>
  <p>Be sure to sign up online for our e-monthly newsletter to receive specials, coupons, exclusive offers, and more!</p>
  <form><div class="field">Enter you email address</div><div class="go">Subscribe</div></form>
</section>

<footer class="foot">
  <div class="cols">
    <div class="col"><h4>GENERAL LINKS</h4><ul><li>Marlow Hall</li><li>Terms &amp; Condition</li><li>Privacy Policy</li><li>Payment &amp; Cancellation Policy</li></ul></div>
    <div class="col"><h4>HELP</h4><ul><li>1800-200-4455 | Toll Free</li><li>care@marlowhall.biz</li></ul></div>
    <div class="col"><h4>SELL WITH US</h4><ul><li>Become an Exhibitor</li><li>Benefits</li></ul></div>
    <div class="col"><h4>FOLLOW</h4><div class="social"><i></i><i></i><i></i><i></i><i></i><i></i></div></div>
    <div class="col"><h4>SHOP WITH<br>CONFIDENCE</h4><div class="cards"><i></i><i></i><i></i><i></i><i></i><i></i></div></div>
  </div>
  <div class="copy">© Copyright 2015 Marlow Hall. All rights reserved.</div>
</footer>

</body>
</html>
```